Quillon’s Prime Response Vehicle Branding

I am looking to get a half wrap for vehicles to assist in branding for a fire water storm and mold restoration company. I would like to have something similar to the photo loaded to include RWTB Certified Firm Logo and we also use Vans and Trucks...

Target Market(s)

Insurance claims damage from fire water floods and storms and mold....

Requirements
Must have
• The listed logo that I have uploaded. I would also like to have the fact of services provided (see below of services provided)
I would like something for the back of trucks / vans also to be included.

Please list where it looks uniform the following:
- Property Damage Restoration Specialist.
- 24 hr Emergency Service
- Web site: Quillonprimeresponse.com
- Office line: 904-618-3927

Services Provided to list:
Fire - Water - Mold - Storm
Restoration
Nice to have
• I would like to have some designs that incorporate in the background showing fire, wind / water / possibly if that can fit into what you design and it does not need to overwhelm the design though...
Should not have
• I do not want the logo changed.
I do not want it to be to busy.

```html
<!DOCTYPE html>
<html lang="en">
<head>
<meta charset="utf-8">
<title>Quillon’s Prime Response – Door Wrap</title>
<link rel="stylesheet" href="https://fonts.googleapis.com/css2?family=Montserrat:wght@700;800;900&display=swap">
<style>
  :root {
    --page: #ffffff;
    --ink: #111111;
    --panel-grey: #e2e2e2;
    --panel-edge: #bdbdbd;
    --tab-grey: #d6d6d6;
    --tab-inner: #e6e6e6;
    --brand-red: #c8201e;
    --storm-blue: #2f6fe4;
    --ember-red: #e5372c;
    --flame-orange: #f08a1c;
    --ring-blue: #3b6fd6;
    --bar-black: #111111;
    --bar-text: #ffffff;
  }
  html, body {
    margin: 0;
    padding: 0;
    width: 1200px;
    height: 424px;
    overflow: hidden;
    background: var(--page);
  }
  .door-wrap {
    position: absolute;
    left: 63px;
    top: 1px;
    width: 1073px;
    height: 422px;
    font-family: 'Montserrat', sans-serif;
  }
  .contact-label { font-weight: 800; font-size: 16px; letter-spacing: 1.5px; fill: var(--ink); }
  .contact-phone { font-weight: 800; font-size: 15px; letter-spacing: 1px; fill: var(--ink); }
  .website { font-weight: 800; font-size: 15px; letter-spacing: 0.6px; fill: var(--ink); }
  .headline { font-weight: 900; font-size: 38px; letter-spacing: 1px; fill: var(--ink); }
  .brand-name { font-weight: 800; font-size: 19px; fill: var(--ink); }
  .badge-big { font-weight: 800; font-size: 16px; fill: var(--ink); }
  .badge-small { font-weight: 800; font-size: 8.5px; fill: var(--ink); }
  .services { font-weight: 800; font-size: 20px; letter-spacing: 1.2px; fill: var(--bar-text); }
</style>
</head>
<body>
<svg class="door-wrap" viewBox="0 0 725 285" xmlns="http://www.w3.org/2000/svg">
  <defs>
    <linearGradient id="elementsGradient" x1="0" y1="0" x2="1" y2="0">
      <stop offset="0" stop-color="#ffffff" stop-opacity="0.2"/>
      <stop offset="0.15" stop-color="var(--storm-blue)"/>
      <stop offset="0.45" stop-color="#7a5fd0"/>
      <stop offset="0.7" stop-color="var(--ember-red)"/>
      <stop offset="1" stop-color="#f6b0a0"/>
    </linearGradient>
    <linearGradient id="elementsFade" x1="0" y1="0" x2="0" y2="1">
      <stop offset="0" stop-color="#ffffff" stop-opacity="0.85"/>
      <stop offset="0.4" stop-color="#ffffff" stop-opacity="0.1"/>
      <stop offset="1" stop-color="#ffffff" stop-opacity="0"/>
    </linearGradient>
    <radialGradient id="flameGlow" cx="0.5" cy="0.55" r="0.5">
      <stop offset="0" stop-color="#ffb347"/>
      <stop offset="0.45" stop-color="var(--flame-orange)" stop-opacity="0.85"/>
      <stop offset="1" stop-color="#ffffff" stop-opacity="0"/>
    </radialGradient>
  </defs>

  <!-- background artwork: fire, water and storm energy -->
  <g class="elements-art" role="img" aria-label="Background artwork of blue water and lightning blending into red and orange fire">
    <rect x="172" y="25" width="553" height="260" fill="url(#elementsGradient)"/>
    <rect x="172" y="25" width="553" height="260" fill="url(#elementsFade)"/>
  </g>

  <!-- soft flame glow where the raised-fist illustration belongs -->
  <rect class="fist-art" role="img" aria-label="Illustration of a raised clenched fist engulfed in flames"
        x="10" y="130" width="150" height="155" fill="url(#flameGlow)"/>

  <!-- contact block -->
  <g class="contact-block">
    <polygon points="0,28 178,28 178,92 150,132 0,132" fill="var(--panel-grey)"/>
    <polyline points="178,92 150,132" stroke="var(--panel-edge)" stroke-width="3" fill="none"/>
    <text class="contact-label" x="22" y="75">OFFICE LINE</text>
    <text class="contact-phone" x="24" y="97">904-618-3927</text>
  </g>

  <!-- brand tab -->
  <g class="brand-tab">
    <polygon points="480,0 725,0 725,85 480,85 445,42" fill="var(--tab-grey)"/>
    <polygon points="486,6 719,6 719,79 486,79 455,42" fill="var(--tab-inner)"/>
    <rect x="490" y="30" width="20" height="20" fill="var(--brand-red)"/>
    <text class="brand-name" x="520" y="37">Quillon’s Prime</text>
    <text class="brand-name" x="520" y="60">Response</text>
  </g>

  <text class="website" x="193" y="93">Quillonprimeresponse.com</text>

  <g class="headline-block">
    <text class="headline" x="193" y="131">Property Damage</text>
    <text class="headline" x="193" y="173">Restoration</text>
    <text class="headline" x="193" y="215">Specialist</text>
  </g>

  <!-- 24/7 emergency badge -->
  <g class="emergency-badge">
    <circle cx="663" cy="180" r="44" fill="#ffffff" fill-opacity="0.75"/>
    <path d="M630,215 A44,44 0 1 1 700,205" fill="none" stroke="var(--ring-blue)" stroke-width="4"/>
    <polygon points="700,197 708,209 694,210" fill="var(--ring-blue)"/>
    <path d="M612,172 q-6,6 -2,16 q10,24 30,34 q10,4 16,-2 l-8,-10 q-4,4 -8,2 q-12,-8 -18,-20 q-2,-4 2,-8 z" fill="var(--ring-blue)"/>
    <text class="badge-big" x="643" y="176">24/7</text>
    <text class="badge-small" x="639" y="190">Emergency</text>
    <text class="badge-small" x="647" y="201">Service</text>
  </g>

  <!-- services bar -->
  <g class="services-bar">
    <rect x="70" y="230" width="610" height="50" rx="25" fill="var(--bar-black)"/>
    <text class="services" x="105" y="262">Fire| Water | Mold | Storm Restoration</text>
  </g>
</svg>
</body>
</html>
```